Lanterne architecture business cards

We are a new company based in New Zealand. We Specialize in High end Luxury Residential Architecture.

Every home is bespoke and is designed to each clients individual requirements and needs.

I like to design buildings that inspire people through light and form while offering a high level of comfort and usability.

Lines of sight, proportion and balance are fundamental to the spaces I create.
Updates

August 5th is current deadline - Today's date is the 13th of August.

Target Market(s)

New Zealanders who want a custom individual home design, typically 30-65 year old males and females

Industry/Entity Type

Architecture

Contact Information for Business Card

Director - Derek Tolson
Contact Number - 0279164073
Email - info@lanternearchitecture-example.co.nz
Webstie - www.lanternearchitecture-example.co.nz
Social Media - @lanternearchitecture

Font styles to use
Sans Serif

Requirements
Must have
• Logo (Both Sides)
Website
Email
Contact Number
Social Media

Nice to have
• Texture
Should not have
• More than 3 colours - typically I would've thought 2 would be good to match the logo.

```html
<!DOCTYPE html>
<html lang="en">
<head>
<meta charset="utf-8">
<title>Lanterne architecture business cards</title>
<link rel="stylesheet" href="https://fonts.googleapis.com/css2?family=Josefin+Sans:wght@300&family=Open+Sans:wght@300;700&family=Arimo:wght@700&display=swap">
<style>
  :root {
    --stage: #ececec;
    --card: #ffffff;
    --texture-light: #ffffff;
    --texture-dark: #f1f1f1;
    --gold: #c8962f;
    --gold-deep: #b07f25;
    --gold-light: #f0c96a;
    --ink: #444444;
    --rule: #a9a9a9;
  }
  * { box-sizing: border-box; margin: 0; padding: 0; }
  html, body { width: 1200px; height: 1200px; overflow: hidden; }
  body { background: var(--stage); position: relative; }

  .card {
    position: absolute;
    width: 793px;
    height: 454px;
    background: var(--card);
    border-radius: 42px;
    overflow: hidden;
  }
  .card--front { left: 204px; top: 102px; }
  .card--back  { left: 204px; top: 645px; }

  .card-texture {
    position: absolute; inset: 0;
    background: linear-gradient(135deg, var(--texture-dark) 0%, var(--texture-light) 70%);
  }

  /* Front */
  .brand-dot {
    position: absolute; left: 336px; top: 59px;
    width: 122px; height: 122px; border-radius: 50%;
    background: var(--gold);
  }
  .wordmark {
    position: absolute; left: 87px; width: 619px;
    display: flex; justify-content: space-between;
    font-family: "Josefin Sans", sans-serif; font-weight: 300;
    color: var(--gold); line-height: 1;
  }
  .wordmark--name { top: 258px; font-size: 62px; }
  .wordmark--trade { top: 324px; font-size: 20px; }
  .tagline {
    position: absolute; left: 0; right: 0; top: 398px;
    text-align: center;
    font-family: "Arimo", sans-serif; font-weight: 700; font-size: 18px;
    color: var(--gold);
  }

  /* Back */
  .back-mark { position: absolute; left: 82px; top: 52px; display: flex; flex-direction: column; align-items: center; gap: 12px; }
  .back-mark__dot { width: 86px; height: 86px; border-radius: 50%; background: var(--gold); }
  .back-mark__name {
    font-family: "Josefin Sans", sans-serif; font-weight: 300; font-size: 26px;
    color: var(--gold); letter-spacing: 2px;
  }
  .person { position: absolute; right: 78px; top: 60px; text-align: right; color: var(--ink); }
  .person__name {
    font-family: "Open Sans", sans-serif; font-weight: 700; font-size: 48px;
    letter-spacing: 5px; line-height: 1;
  }
  .person__role {
    margin-top: 14px;
    font-family: "Open Sans", sans-serif; font-weight: 300; font-size: 42px;
    letter-spacing: 4px; line-height: 1;
  }

  .rule { position: absolute; left: 0; right: 0; height: 2px; }
  .rule--grey { background: linear-gradient(90deg, var(--rule), #c4c4c4 60%, #dcdcdc); }
  .rule--gold {
    height: 4px;
    background: linear-gradient(90deg, var(--gold-deep), var(--gold-light) 60%, var(--gold-deep));
  }

  .contact { position: absolute; left: 81px; top: 327px; font-family: "Arimo", sans-serif; font-weight: 700; font-size: 19px; color: var(--ink); }
  .contact__row { display: flex; align-items: center; height: 30px; margin-bottom: 1px; }
  .contact__item { display: flex; align-items: center; gap: 12px; margin-right: 26px; }
  .icon-box {
    width: 26px; height: 26px; border: 1.5px solid var(--ink);
    display: flex; align-items: center; justify-content: center;
  }
  .icon-box svg { width: 16px; height: 16px; }

  .connect { position: absolute; right: 84px; top: 323px; text-align: right; font-family: "Arimo", sans-serif; font-weight: 700; color: var(--ink); }
  .connect__title { font-size: 19px; }
  .connect__networks { display: flex; justify-content: flex-end; gap: 9px; margin: 14px 0 12px; }
  .connect__network { width: 23px; height: 23px; border-radius: 4px; background: var(--gold); }
  .connect__handle { font-size: 19px; }
</style>
</head>
<body>

<section class="card card--front" aria-label="Card front">
  <div class="card-texture" role="img" aria-label="Faint light grey geometric petal pattern texture"></div>
  <div class="brand-dot"></div>
  <div class="wordmark wordmark--name" aria-label="Lanterne">
    <span>L</span><span>A</span><span>N</span><span>T</span><span>E</span><span>R</span><span>N</span><span>E</span>
  </div>
  <div class="wordmark wordmark--trade" aria-label="Architecture">
    <span>A</span><span>R</span><span>C</span><span>H</span><span>I</span><span>T</span><span>E</span><span>C</span><span>T</span><span>U</span><span>R</span><span>E</span>
  </div>
  <p class="tagline">High end Luxury Residential Architecture.</p>
</section>

<section class="card card--back" aria-label="Card back">
  <div class="card-texture" role="img" aria-label="Faint light grey geometric petal pattern texture"></div>

  <div class="back-mark">
    <div class="back-mark__dot"></div>
    <span class="back-mark__name">Lanterne</span>
  </div>

  <div class="person">
    <h1 class="person__name">DEREK TOLSON</h1>
    <p class="person__role">Director</p>
  </div>

  <div class="rule rule--grey" style="top:209px"></div>
  <div class="rule rule--grey" style="top:226px"></div>
  <div class="rule rule--gold" style="top:254px"></div>
  <div class="rule rule--grey" style="top:284px"></div>
  <div class="rule rule--grey" style="top:300px"></div>

  <div class="contact">
    <div class="contact__row">
      <span class="contact__item">
        <span class="icon-box"><svg viewBox="0 0 16 16"><path d="M8 1.5a4.5 4.5 0 0 0-4.5 4.5c0 3.3 4.5 8.5 4.5 8.5s4.5-5.2 4.5-8.5A4.5 4.5 0 0 0 8 1.5z" fill="none" stroke="#444" stroke-width="1.5"/><circle cx="8" cy="6" r="1.6" fill="#444"/></svg></span>
        New Zealand
      </span>
      <span class="contact__item">
        <span class="icon-box"><svg viewBox="0 0 16 16"><path d="M4 2.5l2 .2 1 3-1.5 1.2c.8 1.6 2 2.8 3.6 3.6L10.3 9l3 1 .2 2c-.5 1-1.5 1.5-2.5 1.3C6.5 12.3 3.7 9.5 2.7 5 2.5 4 3 3 4 2.5z" fill="#444"/></svg></span>
        0279164073
      </span>
    </div>
    <div class="contact__row">
      <span class="contact__item">
        <span class="icon-box"><svg viewBox="0 0 16 16"><rect x="2" y="4" width="12" height="8" fill="#444"/><path d="M2 4l6 5 6-5" fill="none" stroke="#fff" stroke-width="1.2"/></svg></span>
        info@lanternearchitecture-example.co.nz
      </span>
    </div>
    <div class="contact__row">
      <span class="contact__item">
        <span class="icon-box"><svg viewBox="0 0 16 16"><path d="M4 2l8 7H8.5l1.8 4-1.5.7L7 9.7 4 12z" fill="#444"/></svg></span>
        www.lanternearchitecture-example.co.nz
      </span>
    </div>
  </div>

  <div class="connect">
    <p class="connect__title">Let’s connect</p>
    <div class="connect__networks">
      <span class="connect__network"></span>
      <span class="connect__network"></span>
      <span class="connect__network"></span>
      <span class="connect__network"></span>
    </div>
    <p class="connect__handle">@lanternearchitecture</p>
  </div>
</section>

</body>
</html>
```